Modern HomePage Design for Church

We are looking for a modern homepage design using the sections we put together in the template. The colors we want are blue, black, grey, and white. We do not want use the colors in the logo. Please modify the logo color to match the website color scheme.

Target Market(s)

Church

Industry/Entity Type

Church

Number of Pages Required

1 page

Colors
0293ce
ffffff
474747
9d9d9d

```html
<!DOCTYPE html>
<html lang="en">
<head>
<meta charset="utf-8">
<title>Wellspring Community Church</title>
<link href="https://fonts.googleapis.com/css2?family=Lato:ital,wght@0,400;0,700;0,900;1,400;1,700&display=swap" rel="stylesheet">
<style>
:root{
  --blue:#1b6fd0;
  --blue-light:#2a86de;
  --ink:#222222;
  --text:#474747;
  --muted:#9d9d9d;
  --white:#ffffff;
  --dark:#1e1e1e;
  --footer:#2e2e2e;
}
*{margin:0;padding:0;box-sizing:border-box}
html,body{width:1200px;height:3854px;overflow:hidden}
body{font-family:'Lato',sans-serif;color:var(--text);background:var(--white);position:relative}
.abs{position:absolute}
.btn-outline{position:absolute;border:2px solid var(--ink);color:var(--ink);font-size:12px;font-weight:900;letter-spacing:.5px;display:flex;align-items:center;justify-content:center;background:var(--white)}
.btn-blue{position:absolute;background:var(--blue);color:var(--white);font-size:12px;font-weight:700;display:flex;align-items:center;justify-content:center}
.photo{position:absolute}

/* header */
.site-header{position:absolute;left:0;top:0;width:1200px;height:128px;background:var(--white)}
.brand{position:absolute;left:77px;top:44px;display:flex;align-items:center;gap:10px}
.brand-dot{width:22px;height:22px;border-radius:50%;background:var(--blue)}
.brand-name{font-size:20px;font-weight:900;color:var(--blue);line-height:1.1;letter-spacing:.5px}
.nav a{position:absolute;top:56px;font-size:13px;font-weight:700;color:var(--ink);text-decoration:none;letter-spacing:.3px}

/* hero */
.hero{position:absolute;left:0;top:128px;width:1200px;height:535px;background:linear-gradient(160deg,#c9a98a 0%,#7a5a44 40%,#3c2e28 75%,#6a5444 100%)}
.hero h1{position:absolute;left:0;width:1200px;top:205px;text-align:center;color:var(--white);font-size:56px;font-weight:900;line-height:60px;text-shadow:0 2px 8px rgba(0,0,0,.4)}

.visitor-bar{position:absolute;left:0;top:663px;width:1200px;height:75px;background:var(--dark)}
.visitor-bar p{position:absolute;left:283px;top:27px;font-size:14px;color:var(--white)}
.visitor-bar b{margin-right:8px}

/* welcome */
.welcome h2{position:absolute;left:77px;top:795px;font-size:33px;font-weight:900;color:var(--ink)}
.welcome p{position:absolute;left:77px;top:855px;width:600px;font-size:14px;line-height:26px;color:var(--muted)}

/* leader message */
.leader{position:absolute;left:0;top:1118px;width:1200px;height:252px;background:linear-gradient(180deg,#3a322c 0%,#4e4036 55%,#6b5038 100%)}
.leader h3{position:absolute;left:230px;width:300px;top:65px;text-align:center;color:var(--white);font-size:14px;font-weight:900}
.leader .date{position:absolute;left:230px;width:300px;top:96px;text-align:center;color:#ddd;font-size:13px}
.leader .msg{position:absolute;left:230px;width:300px;top:134px;text-align:center;color:#ddd;font-size:13px;line-height:22px}
.count{position:absolute;top:75px;width:90px;text-align:center;color:var(--white)}
.count span{display:block;font-size:11px;font-weight:700}
.count b{display:block;font-size:40px;font-weight:700;line-height:48px}

/* features */
.feature{position:absolute;top:1430px;width:320px;text-align:center}
.feature h4{margin-top:18px;font-size:14px;font-weight:900;color:var(--blue)}
.feature p{margin-top:8px;font-size:13px;line-height:20px;color:var(--muted)}

/* blue panels */
.panel-blue{position:absolute;background:var(--blue);color:var(--white);text-align:center}
.panel-blue h2{font-size:31px;font-weight:900}
.panel-blue p{font-size:13px;line-height:21px}

/* pastor */
.pastor{position:absolute;left:0;top:2477px;width:1200px;height:401px;background:linear-gradient(135deg,#2a2a2a,#1a1a1a 60%,#2c2c2c)}
.pastor h2{position:absolute;top:75px;font-size:28px;font-weight:900;color:var(--white)}
.quote{position:absolute;left:344px;top:130px;width:330px;font-size:19px;font-weight:400;color:var(--blue-light);line-height:24px}
.pastor .bio{position:absolute;left:344px;top:200px;width:330px;font-size:12px;line-height:20px;color:#ccc}
.podcast{position:absolute;left:750px;width:380px;height:50px}
.play{position:absolute;left:0;top:2px;width:34px;height:34px;border:2px solid #ddd}
.play svg{display:block}
.podcast .t{position:absolute;left:54px;top:0;font-size:15px;font-weight:700;color:var(--blue-light);white-space:nowrap}
.podcast .by{position:absolute;left:54px;top:24px;font-size:12px;color:#ddd}

/* events */
.events h2{position:absolute;left:0;width:1200px;top:2925px;text-align:center;font-size:33px;font-weight:900;color:var(--ink)}
.card{position:absolute;top:3002px;width:329px;height:390px}
.card .img{position:absolute;left:0;top:0;width:329px;height:180px}
.badge{position:absolute;left:0;top:0;width:57px;height:62px;background:var(--blue);color:var(--white);text-align:center}
.badge span{display:block;font-size:12px;font-weight:700;margin-top:5px}
.badge b{display:block;font-size:30px;font-weight:900;line-height:32px}
.card h3{position:absolute;left:0;top:196px;font-size:20px;font-weight:700;color:var(--ink);line-height:25px;width:300px}
.meta{position:absolute;left:0;font-size:11px;color:var(--blue);display:flex;align-items:center;gap:10px}
.card .btn-outline{top:349px;left:0;width:134px;height:34px}

/* footer */
.site-footer{position:absolute;left:0;top:3451px;width:1200px;height:347px;background:var(--footer)}
.site-footer h4{position:absolute;top:46px;font-size:18px;font-weight:700;color:var(--white)}
.fitem{position:absolute;width:320px;height:80px}
.fitem .th{position:absolute;left:0;top:0;width:85px;height:78px}
.fitem .t{position:absolute;left:107px;top:0;font-size:15px;font-weight:700;color:var(--blue-light)}
.fitem p{position:absolute;left:107px;top:24px;width:200px;font-size:12px;line-height:18px;color:#ccc}
.tag{position:absolute;border:1px solid #bbb;color:#ddd;font-size:12px;height:26px;padding:0 9px;display:flex;align-items:center}
.feeds{position:absolute;left:437px;top:216px;width:329px;height:93px;background:linear-gradient(180deg,#8f7a63,#5a4a3d);display:flex;align-items:center;justify-content:center;color:var(--white);font-size:20px;font-weight:700}
.bottom-bar{position:absolute;left:0;top:3798px;width:1200px;height:56px;background:var(--dark)}
.bottom-bar p{position:absolute;left:77px;top:20px;font-size:11px;color:#aaa}
.social{position:absolute;top:16px;width:24px;height:24px;background:#bdbdbd;border-radius:3px}
</style>
</head>
<body>

<header class="site-header">
  <div class="brand"><div class="brand-dot"></div><div class="brand-name">WELLSPRING<br><span style="font-size:11px">COMMUNITY CHURCH</span></div></div>
  <nav class="nav">
    <a style="left:318px">HOME</a>
    <a style="left:407px">TEAM</a>
    <a style="left:492px">FEATURES</a>
    <a style="left:607px">EVENTS</a>
    <a style="left:705px">SERMONS</a>
    <a style="left:820px">BLOG</a>
    <a style="left:903px">CONTACT</a>
  </nav>
  <div class="btn-blue" style="left:1007px;top:46px;width:116px;height:36px">GIVE ONLINE</div>
</header>

<section class="hero" role="img" aria-label="Congregation worshipping with raised hands">
  <h1>WELLSPRING<br>COMMUNITY CHURCH</h1>
</section>

<div class="visitor-bar">
  <p><b>First Visitor ?</b> Aliquam malesuada vulputate lectus, sed aliquam erat</p>
  <div class="btn-blue" style="left:784px;top:19px;width:128px;height:36px">VISITORS INFO</div>
</div>

<section class="welcome">
  <div class="photo" role="img" aria-label="Smiling couple sitting on church steps" style="left:578px;top:738px;width:622px;height:380px;background:linear-gradient(90deg,#ffffff 0%,#d9d2c8 25%,#a89a88 60%,#7d7264 100%)"></div>
  <h2>WELCOME TO OUR WEBSITE</h2>
  <p>Aliquam malesuada vulputate lectus, sed aliquam erat commodo et. Nam fringilla tristique consectetur. Duis condimentum id ligula ac rutrum . Duis at neque eget nibh venenatis elementum vestibulum velit in ultricies maximus. Etiam fermentum sed mauris at mattis. Aliquam malesuada vulputate lectus, sed aliquam erat commodo et. Nam fringilla tristique consectetur.</p>
  <div class="btn-outline" style="left:77px;top:1020px;width:130px;height:36px">READ MORE</div>
</section>

<section class="leader" role="img" aria-label="Cross silhouetted against a sunset field">
  <h3>CHURCH LEADER MESSAGE</h3>
  <div class="date">April 12, 2019 7:00pm</div>
  <div class="msg">Sed aliquam erat commodo etnam fringilla tristique consectetur.</div>
  <div class="count" style="left:610px"><span>DAYS</span><b>05</b></div>
  <div class="count" style="left:710px"><span>HOURS</span><b>15</b></div>
  <div class="count" style="left:825px"><span>MINUTES</span><b>32</b></div>
  <div class="count" style="left:947px"><span>SECONDS</span><b>45</b></div>
  <div class="btn-blue" style="left:766px;top:159px;width:128px;height:34px">READ MORE</div>
</section>

<section class="features">
  <div class="feature" style="left:79px">
    <svg width="46" height="42" viewBox="0 0 24 22"><path d="M12 21 2.5 11.5A5.5 5.5 0 0 1 12 3.7a5.5 5.5 0 0 1 9.5 7.8Z" fill="#444"/></svg>
    <h4>WHAT WE BELIVE</h4>
    <p>Aliquam malesuada vulputate lectus,<br>sed aliquam erat commodo etnam fringilla<br>tristique consectetur. Duis condimentum id<br>ligula ac rutrum</p>
  </div>
  <div class="feature" style="left:439px">
    <svg width="34" height="46" viewBox="0 0 18 24"><path d="M9 0a8 8 0 0 1 8 8c0 6-8 16-8 16S1 14 1 8a8 8 0 0 1 8-8Z" fill="#444"/><circle cx="9" cy="8" r="3" fill="#fff"/></svg>
    <h4>SERVICE &amp; LOCATION</h4>
    <p>Aliquam malesuada vulputate lectus,<br>sed aliquam erat commodo etnam fringilla<br>tristique consectetur. Duis condimentum id<br>ligula ac rutrum</p>
  </div>
  <div class="feature" style="left:799px">
    <svg width="46" height="44" viewBox="0 0 24 23"><rect x="1" y="6" width="22" height="5" fill="#444"/><rect x="3" y="12" width="18" height="11" fill="#444"/><rect x="10.5" y="6" width="3" height="17" fill="#fff"/><path d="M12 6C9 0 4 2 7 6M12 6c3-6 8-4 5 0" fill="none" stroke="#444" stroke-width="2"/></svg>
    <h4>GIVING</h4>
    <p>Aliquam malesuada vulputate lectus,<br>sed aliquam erat commodo etnam fringilla<br>tristique consectetur. Duis condimentum id<br>ligula ac rutrum</p>
  </div>
  <div class="btn-outline" style="left:172px;top:1645px;width:134px;height:34px">READ MORE</div>
  <div class="btn-outline" style="left:532px;top:1645px;width:134px;height:34px">READ MORE</div>
  <div class="btn-outline" style="left:892px;top:1645px;width:134px;height:34px">READ MORE</div>
</section>

<section class="involved">
  <div class="photo" role="img" aria-label="Wooden cross in a church interior" style="left:0;top:1727px;width:210px;height:190px;background:linear-gradient(135deg,#a06a3a,#5a3520)"></div>
  <div class="photo" role="img" aria-label="Smiling older woman" style="left:210px;top:1727px;width:390px;height:190px;background:linear-gradient(135deg,#7e7468,#b9a58e 60%,#8d5a3a)"></div>
  <div class="photo" role="img" aria-label="Children in a Sunday school class" style="left:0;top:1917px;width:220px;height:185px;background:linear-gradient(135deg,#c5b0a0,#8a6c5c)"></div>
  <div class="photo" role="img" aria-label="Choir singing in a church" style="left:220px;top:1917px;width:380px;height:185px;background:linear-gradient(135deg,#5c4a3e,#2e2420 60%,#6a3a58)"></div>
  <div class="panel-blue" style="left:600px;top:1727px;width:600px;height:375px">
    <h2 style="margin-top:98px">GET INVOLVED</h2>
    <p style="margin-top:20px">Aliquam malesuada vulputate lectus, sed aliquam erat commodo et.<br>Nam fringilla tristique consectetur. Duis condimentum id ligula ac<br>rutrum . Duis at neque eget nibh venenatis elementum.<br>Ut vestibulum velit in ultricies maximus. Etiam fermentum<br>sed mauris at mattis..</p>
  </div>
</section>

<section class="blog">
  <div class="panel-blue" style="left:0;top:2102px;width:600px;height:375px">
    <h2 style="margin-top:77px">BLOG POSTS</h2>
    <p style="margin-top:14px;font-size:20px;font-weight:700;line-height:26px">Aliquam malesuada vulputate lectus convallis</p>
    <p style="margin-top:12px">Aliquam malesuada vulputate lectus, sed aliquam erat commodo et.<br>Nam fringilla tristique consectetur. Duis condimentum id<br>ligula ac rutrum . Duis at neque eget nibh venenatis elementum.<br>Ut vestibulum velit in ultricies maximus. Etiam fermentum<br>sed mauris at mattis..</p>
  </div>
  <h2 class="abs" style="left:648px;top:2160px;font-size:31px;font-weight:900;color:var(--ink)">PRAY WITHOUT CEASING</h2>
  <p class="abs" style="left:648px;top:2225px;width:480px;font-size:13px;line-height:21px;color:var(--muted)">Aliquam malesuada vulputate lectus, sed aliquam erat commodo et.<br>Nam fringilla tristique consectetur. Duis condimentum id<br>ligula ac rutrum . Duis at neque eget nibh venenatis elementum.<br>Ut vestibulum velit in ultricies maximus. Etiam fermentum<br>sed mauris at mattis..</p>
  <div class="btn-outline" style="left:648px;top:2377px;width:130px;height:36px">READ MORE</div>
</section>

<section class="pastor">
  <h2 style="left:77px">PASTOR</h2>
  <div class="photo" role="img" aria-label="Portrait of the pastor" style="left:77px;top:123px;width:240px;height:227px;background:linear-gradient(135deg,#9a8a78,#4a3e36)"></div>
  <div class="quote">" Malesuada Vulputate malesuada vulputate lectus.."</div>
  <p class="bio">Aliquam ultrices viverra lorem at tempus nibh venenatis.. Duis at neque eget nibh venenatis elementum. Ut vestibulum velit in ultricies maximus. Etiam fermentum sed mauris at mattis eu justo nec nisl rutrum interdum..</p>
  <h2 style="left:750px">PODCASTS</h2>
  <div class="podcast" style="top:123px"><div class="play"><svg width="30" height="30" viewBox="0 0 30 30"><path d="M12 9l8 6-8 6z" fill="#fff"/></svg></div><div class="t">Malesuada Vulputate malesuada...</div><div class="by">By Daniel Reed</div></div>
  <div class="podcast" style="top:217px"><div class="play"><svg width="30" height="30" viewBox="0 0 30 30"><path d="M12 9l8 6-8 6z" fill="#fff"/></svg></div><div class="t">Malesuada Vulputate malesuada...</div><div class="by">By Daniel Reed</div></div>
  <div class="podcast" style="top:310px"><div class="play"><svg width="30" height="30" viewBox="0 0 30 30"><path d="M12 9l8 6-8 6z" fill="#fff"/></svg></div><div class="t">Malesuada Vulputate malesuada...</div><div class="by">By Daniel Reed</div></div>
</section>

<section class="events">
  <h2>UPCOMING EVENTS</h2>
  <article class="card" style="left:77px">
    <div class="img" role="img" aria-label="Seniors reading together at church" style="background:linear-gradient(135deg,#8a7058,#c8b8a4)"></div>
    <div class="badge"><span>APR</span><b>15</b></div>
    <h3>Aliquam malesuada vulputate lectus convallis</h3>
    <div class="meta" style="top:262px"><svg width="12" height="12" viewBox="0 0 12 12"><rect x="1" y="2" width="10" height="9" fill="none" stroke="currentColor"/><path d="M1 5h10" stroke="currentColor"/></svg>Firday, 8:00am - Firday 9:00am</div>
    <div class="meta" style="top:288px"><svg width="12" height="12" viewBox="0 0 12 14"><path d="M6 0a5 5 0 0 1 5 5c0 4-5 9-5 9S1 9 1 5a5 5 0 0 1 5-5Z" fill="currentColor"/></svg>Grace Hall Chapel</div>
    <div class="meta" style="top:314px"><svg width="12" height="12" viewBox="0 0 12 12"><path d="M11 1 1 5l4 2 2 4z" fill="currentColor"/></svg>Street Name Goes Here</div>
    <div class="btn-outline">READ MORE</div>
  </article>
  <article class="card" style="left:437px">
    <div class="img" role="img" aria-label="Women singing during worship" style="background:linear-gradient(135deg,#6e4a3a,#c49a84 60%,#5a3e36)"></div>
    <div class="badge"><span>APR</span><b>15</b></div>
    <h3>Aliquam malesuada vulputate lectus convallis</h3>
    <div class="meta" style="top:262px"><svg width="12" height="12" viewBox="0 0 12 12"><rect x="1" y="2" width="10" height="9" fill="none" stroke="currentColor"/><path d="M1 5h10" stroke="currentColor"/></svg>Firday, 8:00am - Firday 9:00am</div>
    <div class="meta" style="top:288px"><svg width="12" height="12" viewBox="0 0 12 14"><path d="M6 0a5 5 0 0 1 5 5c0 4-5 9-5 9S1 9 1 5a5 5 0 0 1 5-5Z" fill="currentColor"/></svg>Grace Hall Chapel</div>
    <div class="meta" style="top:314px"><svg width="12" height="12" viewBox="0 0 12 12"><path d="M11 1 1 5l4 2 2 4z" fill="currentColor"/></svg>Street Name Goes Here</div>
    <div class="btn-outline">READ MORE</div>
  </article>
  <article class="card" style="left:797px">
    <div class="img" role="img" aria-label="Ornate church sanctuary interior" style="background:linear-gradient(180deg,#4a3a2a,#a8824e 55%,#6a5034)"></div>
    <div class="badge"><span>APR</span><b>15</b></div>
    <h3>Aliquam malesuada vulputate lectus convallis</h3>
    <div class="meta" style="top:262px"><svg width="12" height="12" viewBox="0 0 12 12"><rect x="1" y="2" width="10" height="9" fill="none" stroke="currentColor"/><path d="M1 5h10" stroke="currentColor"/></svg>Firday, 8:00am - Firday 9:00am</div>
    <div class="meta" style="top:288px"><svg width="12" height="12" viewBox="0 0 12 14"><path d="M6 0a5 5 0 0 1 5 5c0 4-5 9-5 9S1 9 1 5a5 5 0 0 1 5-5Z" fill="currentColor"/></svg>Grace Hall Chapel</div>
    <div class="meta" style="top:314px"><svg width="12" height="12" viewBox="0 0 12 12"><path d="M11 1 1 5l4 2 2 4z" fill="currentColor"/></svg>Street Name Goes Here</div>
    <div class="btn-outline">READ MORE</div>
  </article>
</section>

<footer class="site-footer">
  <h4 style="left:77px">Latest Sermons</h4>
  <h4 style="left:437px">Sermons Tags</h4>
  <h4 style="left:794px">Latest News</h4>
  <div class="fitem" style="left:77px;top:96px"><div class="th" role="img" aria-label="Sermon thumbnail" style="background:linear-gradient(135deg,#b89c86,#6a5444)"></div><div class="t">Malesuada Vulputate</div><p>Aliquam ultrices viverra lorem at tempus nibh venenatis..</p></div>
  <div class="fitem" style="left:77px;top:206px"><div class="th" role="img" aria-label="Sermon thumbnail" style="background:linear-gradient(135deg,#a0622e,#4a2e1e)"></div><div class="t">Malesuada Vulputate</div><p>Aliquam ultrices viverra lorem at tempus nibh venenatis..</p></div>
  <div class="tag" style="left:437px;top:92px">Cras nisi</div>
  <div class="tag" style="left:532px;top:92px">Metus</div>
  <div class="tag" style="left:602px;top:92px">Gravida</div>
  <div class="tag" style="left:671px;top:92px">Congue</div>
  <div class="tag" style="left:437px;top:130px">Nec</div>
  <div class="tag" style="left:491px;top:130px">Tempusut</div>
  <div class="tag" style="left:575px;top:130px">Massa</div>
  <div class="tag" style="left:640px;top:130px">Proin</div>
  <div class="tag" style="left:437px;top:168px">Tempusut</div>
  <div class="tag" style="left:527px;top:168px">Massa</div>
  <div class="tag" style="left:595px;top:168px">Proin</div>
  <div class="feeds" role="img" aria-label="Cross against an evening sky">Audio Feeds</div>
  <div class="fitem" style="left:794px;top:96px"><div class="th" role="img" aria-label="News thumbnail" style="background:linear-gradient(135deg,#c8b4a2,#7a6452)"></div><div class="t">Malesuada Vulputate</div><p>Aliquam ultrices viverra lorem at tempus nibh venenatis..</p></div>
  <div class="fitem" style="left:794px;top:206px"><div class="th" role="img" aria-label="News thumbnail" style="background:linear-gradient(135deg,#5a4a52,#2a2028)"></div><div class="t">Malesuada Vulputate</div><p>Aliquam ultrices viverra lorem at tempus nibh venenatis..</p></div>
</footer>

<div class="bottom-bar">
  <p>Copyright © 2019 Company Name. All Rights Reserved.</p>
  <div class="social" style="left:964px"></div>
  <div class="social" style="left:1010px"></div>
  <div class="social" style="left:1056px"></div>
  <div class="social" style="left:1100px"></div>
</div>

</body>
</html>
```